Colour and Style Workshop

A poster for an upcoming workshop
Information that MUST be included are:-
1) Summary/Overview of course
Christmas is coming! Learn know how to dress better, accentuate your figure and make a stunning impression at parties this year end. Join our Colour and Style workshop conducted by renowned Designer Marcus Leroy, a familiar name in Singapore’s fashion scene and has been a judge of Velton Bright Studio since the competition’s first run in 2010. He is the Vice President of the Loom and Apparel Council (Singapore), Chairman of its Makers and Sellers Circle and Singapore’s representative to the Orient Couture League. Leroy also sits on the working committee that oversees KOVAL step STEP, Singapore’s fashion incubator project, which has helped launch at least 50 homegrown labels, including rio.belk and IVY RUSK.
Course title: PKV Provide Colour and Style Coordination for Textile and Fashion Industry
Date: 16 and 23 November 2013
Time: 8.30am - 6.30pm
Venue: Harbour Court, 517 Kembang Sari Road, #09-12, Singapore 174295
Course fees: $50 (after 90% funding from LFB for Singaporeans and SPRs)
Registration details – Kembang sari Court Customer service counter, Level 2 or email us at enquiry@lumora-hub.org.
Shoppers who spends $20 and above in Kembang Sari Court will receive a $20 Orient Arcade voucher when they register at the Customer Service Counter.
For more information about our courses and schedule, visit www.lumora-hub.org
Logos (some are just low res files) to include:-
• LuM.hb
• PKL (to use a place holder for now)
• LFB
• Orient Arcade
SIZE of poster is A2.
Target Market(s)
Mostly ladies, shoppers.
20-50 years old
Industry/Entity Type
Fashion
Look and feel

```html
<!DOCTYPE html>
<html lang="en">
<head>
<meta charset="utf-8">
<title>Colour and Style Workshop</title>
<link href="https://fonts.googleapis.com/css2?family=Anton&family=Arimo:wght@400;700&display=swap" rel="stylesheet">
<style>
  :root {
    --red: #e8141b;
    --ink: #111111;
    --paper: #ffffff;
    --frame: #f3c9c9;
    --maroon: #8c1c2c;
    --violet: #6b2a8f;
  }
  * { margin: 0; padding: 0; box-sizing: border-box; }
  html, body { width: 843px; height: 1200px; overflow: hidden; background: var(--paper); }
  .poster {
    position: relative; width: 843px; height: 1200px; overflow: hidden;
    font-family: "Arimo", Arial, sans-serif; color: var(--ink);
    background:
      radial-gradient(ellipse 520px 420px at 120px 60px, rgba(247,197,74,.75), rgba(250,220,150,.35) 55%, rgba(255,255,255,0) 80%),
      radial-gradient(ellipse 300px 260px at 40px 420px, rgba(250,200,120,.35), rgba(255,255,255,0) 75%),
      var(--paper);
  }
  .frame {
    position: absolute; left: 19px; top: 24px; width: 808px; height: 1160px;
    border: 3px solid var(--frame); opacity: .8;
  }
  .decor-ornaments { position: absolute; left: 630px; top: 0; width: 213px; height: 350px; }
  .figure-art { position: absolute; left: 492px; top: 240px; width: 180px; height: 595px; }
  .headline {
    position: absolute; left: 48px; top: 77px; white-space: nowrap;
    font-size: 66px; font-weight: 400; letter-spacing: -0.5px; line-height: 1;
  }
  .workshop-row {
    position: absolute; top: 164px; left: 56px; width: 620px;
    font-size: 31.5px; line-height: 1;
  }
  .workshop-row span { position: absolute; top: 0; white-space: nowrap; }
  .hook {
    position: absolute; left: 52px; top: 214px; white-space: nowrap;
    font-family: "Anton", Impact, sans-serif; font-weight: 400; color: var(--red);
    font-size: 61px; line-height: 78px; letter-spacing: 0.6px;
    text-shadow: 3px 3px 0 #3a3a3a;
  }
  .body-copy {
    position: absolute; left: 56px; top: 383px; white-space: nowrap;
    font-size: 17.8px; line-height: 21.4px;
  }
  .body-copy p + p { margin-top: 21.4px; }
  .course-label {
    position: absolute; left: 55px; top: 720px;
    font-family: "Anton", Impact, sans-serif; color: var(--red); font-size: 24px; line-height: 1.2;
  }
  .course-title {
    position: absolute; left: 55px; top: 751px; white-space: nowrap;
    font-family: "Anton", Impact, sans-serif; font-size: 23px; line-height: 29.5px; letter-spacing: 0.3px;
  }
  .details {
    position: absolute; left: 55px; top: 823px; white-space: nowrap;
    font-size: 21.8px; line-height: 27.5px;
  }
  .details b { font-weight: 700; }
  .details small { font-size: 14.5px; }
  .registration {
    position: absolute; left: 55px; top: 952px; white-space: nowrap;
    font-size: 21.8px; line-height: 27px;
  }
  .promo-bubble { position: absolute; left: 570px; top: 580px; width: 265px; height: 290px; }
  .promo-text {
    position: absolute; left: 583px; top: 614px; width: 240px; white-space: nowrap;
    color: var(--paper); text-align: center; font-size: 17.6px; line-height: 23.1px;
  }
  .info-box {
    position: absolute; left: 20px; top: 1043px; width: 321px; height: 91px;
    background: var(--red); color: var(--paper); white-space: nowrap;
    padding: 5px 0 0 31px; font-size: 21px; line-height: 27px;
  }
  .partner {
    position: absolute; top: 1080px; display: flex; align-items: center; gap: 6px;
    font-size: 16px; font-weight: 700; line-height: 20px; white-space: nowrap;
  }
  .partner .mark { width: 14px; height: 14px; flex: none; }
  .partner--arcade { left: 392px; color: var(--maroon); }
  .partner--arcade .mark { background: var(--maroon); }
  .partner--academy { left: 552px; color: var(--ink); }
  .partner--academy .mark { background: var(--ink); border-radius: 50%; }
  .partner--agency { left: 690px; color: var(--violet); }
  .partner--agency .mark { background: var(--violet); }
</style>
</head>
<body>
<main class="poster">
  <div class="frame"></div>

  <svg class="decor-ornaments" viewBox="0 0 213 350" role="img" aria-label="Red ribbon with three hanging red Christmas baubles tied with gold bows">
    <defs>
      <radialGradient id="ornamentGlow" cx="60%" cy="45%" r="60%">
        <stop offset="0" stop-color="#d8262a" stop-opacity=".55"/>
        <stop offset=".6" stop-color="#e8555a" stop-opacity=".25"/>
        <stop offset="1" stop-color="#ffffff" stop-opacity="0"/>
      </radialGradient>
    </defs>
    <rect width="213" height="350" fill="url(#ornamentGlow)"/>
  </svg>

  <svg class="figure-art" viewBox="0 0 180 595" role="img" aria-label="Black silhouette of a stylish woman walking with a handbag">
    <defs>
      <linearGradient id="figureTone" x1="0" y1="0" x2="0" y2="1">
        <stop offset="0" stop-color="#2a2a2a" stop-opacity=".25"/>
        <stop offset=".5" stop-color="#1a1a1a" stop-opacity=".35"/>
        <stop offset="1" stop-color="#2a2a2a" stop-opacity=".15"/>
      </linearGradient>
    </defs>
    <rect width="180" height="595" rx="60" fill="url(#figureTone)"/>
  </svg>

  <h1 class="headline">Christmas is coming!</h1>
  <div class="workshop-row">
    <span style="left:0">workshop!!!</span>
    <span style="left:217px">workshop!!!</span>
    <span style="left:434px">workshop!!!</span>
  </div>

  <h2 class="hook">Learn know how<br>to dress better,</h2>

  <div class="body-copy">
    <p>accentuate your figure and make a stunning<br>impression at parties this year end. Join our Colour<br>and Style workshop conducted by renowned Designer<br>Marcus Leroy, a familiar name in Singapore’s fashion<br>scene and has been a judge of Velton Bright Studio<br>since the competition’s first run in 2010.</p>
    <p>He is the Vice President of the Loom and Apparel<br>Council (Singapore), Chairman of its Makers and<br>Sellers Circle and Singapore’s representative to the<br>Orient Couture League. Leroy also sits on the<br>working committee that oversees KOVAL step STEP,<br>Singapore’s fashion incubator project, which has<br>helped launch at least 50 homegrown labels, including<br>rio.belk and IVY RUSK.</p>
  </div>

  <div class="course-label">Course title:</div>
  <div class="course-title">PKV Provide Colour and Style Coordination for<br>Textile and Fashion Industry</div>

  <div class="details">
    <b>Date:</b> 16 and 23 November 2013<br>
    <b>Time:</b> 8.30am - 6.30pm<br>
    <b>Venue:</b> Harbour Court, 517 Kembang Sari Road, #09-12, Singapore 174295<br>
    <b>Course fees:</b> $50 <small>(after 90% funding from LFB for Singaporeans and SPRs)</small>
  </div>

  <p class="registration"><b>Registration details</b> : Kembang sari Court Customer service counter,<br>Level 2 or email us at enquiry@lumora-hub.org.</p>

  <svg class="promo-bubble" viewBox="0 0 265 290" aria-hidden="true">
    <circle cx="133" cy="140" r="128" fill="#e8141b"/>
    <polygon points="200,240 258,170 240,286" fill="#e8141b"/>
  </svg>
  <p class="promo-text">Shoppers who<br>spends $20 and<br>above in<br>Kembang Sari Court will<br>receive a $20<br>Orient Arcade voucher<br>when they register at the<br>Customer Service<br>Counter.</p>

  <div class="info-box">For more information about<br>our courses and schedule,<br>visit www.lumora-hub.org</div>

  <div class="partner partner--arcade"><span class="mark"></span>Orient Arcade</div>
  <div class="partner partner--academy"><span class="mark"></span>LuM.hb</div>
  <div class="partner partner--agency"><span class="mark"></span>LFB</div>
</main>
</body>
</html>
```